Community Legal Website

The website is about a law in legal area (Fiscal), it has a moderator and the community also contributes with information.

Attention that this is not for a Law Firm. This is a community site where all the lawyers can contribute wiith their knowledge and at the same time where they can read the Official Law in the fiscal area.

The site is in portuguese, but we have attach information in english about the functionalities.

I attach information which represents the first version of the site done by html.. That is the site we intend to improve.

The site is quite simple because the main pages are:
- Home page;
- Section page (which has the Chapters and articles)
- Article page;

This pages all belong to the article:

redaccao_actual.htm, redaccoes_anteriores.htm, anotacoes.htm, jurisprudencia.htm, decisoesadministrativas.htm, minutas.htm, duvidas.htm

AS you see in all of them the options are always there.

The most important in this site is the usability of the content:

The FAQ, Contacts, Terms of conditions, who we are, are links less important.

Also there is a possibility to have in the homepage a higligh of certain articles that we want to raise from the others.

Please check the excel sheet as well as the zip file wich has the site in portuguese that you can use a website translator to check in your language.
Updates

We added a excel sheet with the functionalities in english which the site must have.

Reason: Because this is easter time we have increased the time for the deliver

Please check briefing update.

Reason: There were some request to extend the deadline because of the Easter

Hi!

Please read carefully the briefing. People are presenting me company web sites adn this is NOT a company web site. THis is a Site wich has a content of Laws. Please check the 1st version in the zip file and improve it. The options are there and you can translate in google tradutor or reading the excel sheet attach.

txs,
KM

Reason: My client need more desing choices

Target Market(s)

Lawyers, jurists and people related with the fiscal Law.

Industry/Entity Type

Legal

Requirements
Must have
• The interface should be clean and elegant.
It should also contribute to speed.
And try to avoid to many distract elements.
The site will be dinamic and with a backoffice, so in that you have to be carefully with the space dynamic. But you don't have to worry about the backoffice. Only the front office which is the public site.

```html
<!DOCTYPE html>
<html lang="pt">
<head>
<meta charset="utf-8">
<title>SERRA VALENTE.net – Legislação Anotada</title>
<link href="https://fonts.googleapis.com/css2?family=Open+Sans:wght@300;400;600&display=swap" rel="stylesheet">
<style>
  :root {
    --ink: #3d5458;
    --ink-soft: #5e6466;
    --slate: #5c6e71;
    --slate-edge: #46585b;
    --aqua: #bff9f7;
    --aqua-edge: #a9e6e3;
    --row: #f8f8f8;
    --arrow-muted: #ececec;
    --white: #ffffff;
  }
  * { box-sizing: border-box; margin: 0; padding: 0; }
  html, body { width: 1200px; height: 573px; overflow: hidden; background: var(--white); }
  body { font-family: "Open Sans", Arial, sans-serif; color: var(--ink-soft); position: relative; }

  .site-header { height: 60px; position: relative; }
  .brand { position: absolute; left: 294px; top: 16px; display: flex; align-items: center; gap: 22px; }
  .brand-square { width: 26px; height: 26px; background: var(--ink); }
  .brand-name { font-size: 20px; font-weight: 300; color: var(--ink); letter-spacing: 0.2px; }
  .main-nav { position: absolute; left: 574px; top: 15px; display: flex; }
  .main-nav a { display: block; height: 31px; line-height: 31px; padding: 0 11px; font-size: 10px; color: #7a8082; text-decoration: none; margin-right: 2px; }
  .main-nav a.is-active { background: var(--aqua); color: var(--ink); }

  .section-band { height: 52px; background: var(--aqua); border-top: 1px solid var(--aqua-edge); text-align: center; }
  .section-band h2 { font-size: 24px; font-weight: 300; line-height: 52px; color: var(--ink); letter-spacing: 0.3px; }

  .law-list { list-style: none; width: 612px; margin: 13px auto 0; }
  .law-list li { height: 37px; margin-bottom: 7px; background: var(--row); border-radius: 2px; display: flex; align-items: center; justify-content: space-between; padding: 0 18px 0 14px; font-size: 11px; color: var(--ink-soft); }
  .law-list li.is-active { background: var(--slate); border: 1px solid var(--slate-edge); color: var(--white); font-weight: 600; }
  .law-list li svg { width: 18px; height: 16px; fill: var(--arrow-muted); }
  .law-list li.is-active svg { fill: var(--white); }

  .fiscal { margin-bottom: 29px; }
  .fiscal .law-list { margin-bottom: 0; }
  .administrative { margin-top: 0; }

  .site-footer { position: absolute; left: 0; top: 488px; width: 1200px; height: 85px; background: var(--slate); border-top: 1px solid var(--slate-edge); }
  .copyright { position: absolute; left: 0; width: 1200px; top: 22px; text-align: center; font-size: 7.5px; color: var(--white); }
  .contact-button { position: absolute; left: 806px; top: 12px; width: 100px; height: 31px; background: var(--aqua); border-radius: 2px; display: flex; align-items: center; justify-content: center; gap: 18px; font-size: 10px; color: #222; text-decoration: none; }
  .contact-button svg { width: 13px; height: 9px; fill: var(--ink); }
</style>
</head>
<body>
  <header class="site-header">
    <div class="brand">
      <span class="brand-square"></span>
      <span class="brand-name">SERRA VALENTE.net</span>
    </div>
    <nav class="main-nav">
      <a href="#" class="is-active">Termos de utilização</a>
      <a href="#">Perguntas frequentes</a>
      <a href="#">Quem somos</a>
      <a href="#">Contactos</a>
    </nav>
  </header>

  <section class="fiscal">
    <div class="section-band"><h2>LEGISLAÇÃO FISCAL ANOTADA</h2></div>
    <ul class="law-list">
      <li>Código do IRS - Imposto sobre o Rendimento das Pessoas Singulares<svg viewBox="0 0 18 16"><path d="M0 5h9V0l9 8-9 8v-5H0z"/></svg></li>
      <li class="is-active">Código do IRC - Imposto sobre o Rendimento das Pessoas Colectivas<svg viewBox="0 0 18 16"><path d="M0 5h9V0l9 8-9 8v-5H0z"/></svg></li>
      <li>Código do IMI - Imposto Municipal sobre Imóveis<svg viewBox="0 0 18 16"><path d="M0 5h9V0l9 8-9 8v-5H0z"/></svg></li>
      <li>RCPIT - Regulamento Complementar do Procedimento de Inspecção Tributária<svg viewBox="0 0 18 16"><path d="M0 5h9V0l9 8-9 8v-5H0z"/></svg></li>
    </ul>
  </section>

  <section class="administrative">
    <div class="section-band"><h2>LEGISLAÇÃO ADMINISTRATIVA ANOTADA</h2></div>
    <ul class="law-list">
      <li>CPTA - Código do Procedimento nos Tribunais Administrativos<svg viewBox="0 0 18 16"><path d="M0 5h9V0l9 8-9 8v-5H0z"/></svg></li>
    </ul>
  </section>

  <footer class="site-footer">
    <p class="copyright">© SERRA VALENTE - 2013</p>
    <a href="#" class="contact-button">CONTACT<svg viewBox="0 0 13 9"><path d="M0 0h13L6.5 5z"/><path d="M0 1.2l6.5 5 6.5-5V9H0z"/></svg></a>
  </footer>
</body>
</html>
```